Bakery Replacement Lighted Sign Face

We are opening a new bakery that sells only cakes. The name is "The Willow Lantern." We are replacing the current sign face with a new look that states our name and makes a bold statement of fun. We will be known for having 101 cakes that are always ready for immediate pickup or delivery. Our colors are pink, orange, and lime green. An image is provided to see the colors.

Target Market(s)

people who buy cakes for parties and all other occasions

Industry/Entity Type

Cakes

Other font styles liked:
• look at the logo and file for the main font name

Colors
59FF00
82FF00
B8FF75
E3FFCB
F4FFEA
F0912C
F2A743
F7CA91
FBE8D2
FDF5EE
EB3D1F
EC4F4E
F09395
F8D3D4
FCEDEE

Requirements
Must have
• The name of the bakery. Logo can be used as is or changed as shown in one of the uploaded PDFs. Must use either pink, orange, lime green, white, or black. We prefer a bright pink background with white lettering as our first choice, but are willing to be open minded to see all creative concepts. Also the sign is 14 feet long and 42 inches tall so the artwork must fit within those boundaries. Also keep in mind the sign does have a 4 inch black frame. So the graphics area is actually 13 feet 2 inches by 3 feet. Also, in the attached pdf that shows a rough possible layout, the words "101 cakes to go" is on the sign. It is NOT a must. Only use the wording if it adds to your design.
Nice to have
• You are welcome to add additional stars or other fun graphics that could look good.
Should not have
• No images of cakes or other bakery products.

```html
<!DOCTYPE html>
<html lang="en">
<head>
<meta charset="utf-8">
<title>The Willow Lantern – Sign Face</title>
<link href="https://fonts.googleapis.com/css2?family=Fredoka:wght@500;600;700&display=swap" rel="stylesheet">
<style>
  :root {
    --canvas: #ffffff;
    --pink: #d81b5c;
    --orange: #f0912c;
    --lime: #7cc242;
    --white: #ffffff;
  }
  html, body {
    margin: 0;
    padding: 0;
    width: 1200px;
    height: 348px;
    overflow: hidden;
    background: var(--canvas);
  }
  .sign {
    position: relative;
    width: 1200px;
    height: 348px;
    font-family: "Fredoka", sans-serif;
    color: var(--white);
  }
  .sign-art {
    position: absolute;
    inset: 0;
  }
  .brand-name {
    position: absolute;
    left: 100px;
    top: 84px;
    margin: 0;
    display: flex;
    align-items: baseline;
    gap: 40px;
    font-weight: 600;
    color: var(--white);
    line-height: 1;
    white-space: nowrap;
  }
  .brand-name .lead {
    font-size: 92px;
    letter-spacing: -0.01em;
  }
  .brand-name .tail {
    font-size: 58px;
    letter-spacing: 0.32em;
  }
  .tagline-pill {
    position: absolute;
    left: 921px;
    top: 93px;
    width: 186px;
    height: 33px;
    border-radius: 17px;
    background: var(--lime);
    display: flex;
    align-items: center;
    justify-content: center;
    font-size: 21px;
    font-weight: 700;
    letter-spacing: 0.01em;
  }
  .service {
    position: absolute;
    left: 641px;
    top: 236px;
    margin: 0;
    font-size: 22px;
    font-weight: 700;
    line-height: 1;
    letter-spacing: 0.04em;
    text-transform: uppercase;
  }
  .service span { display: block; margin-bottom: 4px; }
  .social-handle {
    position: absolute;
    left: 931px;
    top: 250px;
    margin: 0;
    font-size: 16px;
    font-weight: 600;
    letter-spacing: 0.01em;
  }
</style>
</head>
<body>
  <main class="sign">
    <svg class="sign-art" width="1200" height="348" viewBox="0 0 1200 348" xmlns="http://www.w3.org/2000/svg">
      <rect class="sign-field" x="59" y="51" width="1091" height="248" fill="var(--pink)" role="img" aria-label="Bright pink sign field with a soft repeating star pattern"/>
      <path class="service-band" d="M541 220 H1150 V299 H497 C520 278 535 250 541 220 Z" fill="var(--orange)"/>
      <g class="stopwatch-icon" transform="translate(604 260)">
        <circle r="28" fill="var(--white)"/>
        <circle r="19" fill="none" stroke="var(--pink)" stroke-width="3"/>
        <rect x="-5" y="-26" width="10" height="4" rx="1.5" fill="var(--pink)"/>
        <line x1="0" y1="-22" x2="0" y2="-19" stroke="var(--pink)" stroke-width="3"/>
        <line x1="0" y1="0" x2="-6" y2="-9" stroke="var(--pink)" stroke-width="2" stroke-linecap="round"/>
        <line x1="0" y1="0" x2="8" y2="0" stroke="var(--pink)" stroke-width="2" stroke-linecap="round"/>
        <circle r="2" fill="var(--pink)"/>
      </g>
      <circle class="social-dot" cx="901" cy="260" r="22" fill="var(--white)"/>
    </svg>

    <h1 class="brand-name"><span class="lead">The Willow</span><span class="tail">LANTERN</span></h1>
    <div class="tagline-pill">101 cakes to go</div>
    <p class="service"><span>Immediate Pickup</span><span>or Delivery</span></p>
    <p class="social-handle">#willowlanterncakes</p>
  </main>
</body>
</html>
```